Winery Section 199

We need a flyer design for our Accounting Firm that details the benefits of Internal Revenue Code Section 199. This will be marketed to Wineries and Vineyard Farmers We would like to see designs that are bold and utilize our logo and vineyard/winery type symbols colors.

SEE NEW COPY

Target Market(s)

US based wineries and vineyards, Targeting the owners of these companies

Industry/Entity Type

Accounting

Font styles to use
Decorative

Requirements
Must have
• one page - would like to be able to embed into email if possible.
I attached a bunch of logo files only because I don't know which type you need
Nice to have
• see the wording I attached, this is what I would like it to say in general - ok for you to edit if you like. (file 5)

```html
<!DOCTYPE html>
<html lang="en">
<head>
<meta charset="utf-8">
<title>Winery Section 199 Flyer</title>
<link href="https://fonts.googleapis.com/css2?family=Crimson+Pro:wght@300;400&family=Tinos:wght@400;700&display=swap" rel="stylesheet">
<style>
  :root {
    --page: #ffffff;
    --ink-black: #000000;
    --wine-red: #c1121c;
    --band-red: #b0000d;
    --band-dark: #6a0207;
    --white: #ffffff;
    --navy: #1f3a78;
    --display: "Crimson Pro", "Times New Roman", serif;
    --body: "Tinos", "Times New Roman", serif;
  }
  * { margin: 0; padding: 0; box-sizing: border-box; }
  html, body { width: 1200px; height: 1200px; overflow: hidden; background: var(--page); }
  .flyer {
    position: absolute; left: 198px; top: 80px; width: 804px; height: 1040px;
    background: var(--ink-black); overflow: hidden;
  }
  .pour-photo {
    position: absolute; left: 0; top: 0; width: 560px; height: 1040px;
    background:
      radial-gradient(ellipse 230px 300px at 150px 820px, rgba(205,20,30,0.95), rgba(120,0,10,0.55) 60%, rgba(0,0,0,0) 100%),
      radial-gradient(ellipse 110px 320px at 200px 340px, rgba(170,20,25,0.75), rgba(0,0,0,0) 100%),
      linear-gradient(125deg, rgba(230,230,220,0.4) 0%, rgba(70,70,60,0.25) 18%, rgba(0,0,0,0) 42%);
  }
  .band { position: absolute; left: 0; width: 804px; }
  .band-top { top: 492px; height: 51px; background: var(--band-dark); opacity: 0.88; }
  .band-main { top: 543px; height: 233px; background: var(--band-red); opacity: 0.9; }
  .band-bottom { top: 776px; height: 52px; background: var(--band-dark); opacity: 0.88; }

  .headline {
    position: absolute; right: 64px; top: 26px; text-align: right;
    font-family: var(--display); font-weight: 300; color: var(--wine-red);
    font-size: 108px; line-height: 1; letter-spacing: -3px;
  }
  .subhead {
    position: absolute; right: 64px; top: 136px; text-align: right;
    font-family: var(--display); font-weight: 300; color: var(--white);
    font-size: 54px; line-height: 1; letter-spacing: -0.5px;
  }
  .intro {
    position: absolute; left: 426px; top: 228px; width: 312px;
    font-family: var(--body); color: var(--white); font-size: 19px; line-height: 24.6px;
    text-align: justify; letter-spacing: -0.3px;
  }
  .intro p + p { margin-top: 24.6px; }
  .offer {
    position: absolute; left: 42px; top: 564px; width: 704px;
    font-family: var(--body); color: var(--white); font-size: 15.8px; line-height: 22px;
    letter-spacing: -0.1px;
  }
  .offer p + p { margin-top: 22px; }
  .offer strong { font-weight: 700; }

  .contact {
    position: absolute; left: 414px; top: 860px; width: 331px; height: 180px;
    background: var(--white); text-align: center; font-family: var(--body);
  }
  .contact-call { margin-top: 11px; color: var(--wine-red); font-size: 13px; line-height: 16px; }
  .contact-phone { color: var(--navy); font-size: 38px; line-height: 42px; }
  .contact-email { color: var(--wine-red); font-size: 12px; line-height: 15px; }
  .firm-name {
    margin-top: 26px; color: var(--navy); font-family: var(--body);
    font-size: 24px; line-height: 28px;
  }
</style>
</head>
<body>
  <main class="flyer">
    <div class="pour-photo" role="img" aria-label="Photo of red wine pouring from a bottle into a glass"></div>
    <div class="band band-top"></div>
    <div class="band band-main"></div>
    <div class="band band-bottom"></div>

    <h1 class="headline">Pour a glass,</h1>
    <h2 class="subhead">you’re entitled to...</h2>

    <section class="intro">
      <p>Have you made the decision to keep jobs in the US by hiring here in the United States?</p>
      <p>Are you seeing profits as a result of this decision and other smart moves you’ve made while pursuing your passion in the Winemaking and Vineyard field?</p>
    </section>

    <section class="offer">
      <p>You should be taking advantage of the <strong>9% Domestic Production Activities Deduction</strong> the <strong>IRS</strong> has offered available only to <strong>Profitable Wineries and Farmers</strong> located in the US paying wages in the US!</p>
      <p>You do not have to spend any additional funds of your hard earned profits to take advantage of this incredible deduction!&nbsp; Keep more money to grow your business or your retirement account.</p>
      <p>We would love to meet with you and explain how your profitable company can pay less taxes, and claim refunds from previous years with this outstanding deduction.</p>
    </section>

    <aside class="contact">
      <p class="contact-call">Call Dana Hollis at</p>
      <p class="contact-phone">555-014-2290</p>
      <p class="contact-email">dana@larkfieldtax.net</p>
      <p class="firm-name">Larkfield Tax Advisors</p>
    </aside>
  </main>
</body>
</html>
```